Book Cover

Book Title: THE QUIET LEDGER
Book Sub Title: Notes on slowing the daily rush and shaping a calmer household rhythm
Vibe: Professional, stylish, trustworthy (high-end men's fashion)
Website (for inspiration): www.brindlequarry.com
Attached: a potential photo to use for the cover, but open to other options (from our website)

```html
<!DOCTYPE html>
<html lang="en">
<head>
<meta charset="utf-8">
<title>The Quiet Ledger — Book Cover</title>
<link href="https://fonts.googleapis.com/css2?family=Abril+Fatface&family=Playfair+Display:wght@400;500&display=swap" rel="stylesheet">
<style>
  :root {
    --backdrop: #d7d7d7;
    --paper: #ffffff;
    --ink: #0b0b0b;
    --gold: #c4a876;
    --photo-light: #d9c7bd;
    --photo-mid: #c6b0a4;
    --photo-deep: #a8968c;
    --white: #ffffff;
  }
  * { margin: 0; padding: 0; box-sizing: border-box; }
  html, body {
    width: 1200px;
    height: 3000px;
    overflow: hidden;
    background: var(--backdrop);
  }
  .canvas {
    position: relative;
    width: 1200px;
    height: 3000px;
  }
  .cover {
    position: absolute;
    left: 100px;
    top: 852px;
    width: 1000px;
    height: 1296px;
    background: var(--paper);
    overflow: hidden;
  }
  .cover-photo {
    position: absolute;
    left: 266px;
    top: 49px;
    width: 686px;
    height: 1198px;
    background:
      radial-gradient(ellipse at 55% 30%, var(--photo-light) 0%, transparent 60%),
      linear-gradient(160deg, var(--photo-mid) 0%, var(--photo-light) 55%, var(--photo-deep) 100%);
  }
  .title-primary {
    position: absolute;
    left: 104px;
    top: 52px;
    height: 780px;
    writing-mode: vertical-rl;
    font-family: "Abril Fatface", "Playfair Display", serif;
    font-size: 118px;
    line-height: 1;
    color: var(--ink);
    letter-spacing: 0.01em;
    word-spacing: 0.12em;
    white-space: nowrap;
  }
  .title-accent {
    position: absolute;
    left: 262px;
    top: 40px;
    writing-mode: vertical-rl;
    font-family: "Playfair Display", serif;
    font-weight: 400;
    font-size: 168px;
    line-height: 1;
    color: var(--white);
    letter-spacing: 0.06em;
    white-space: nowrap;
  }
  .subtitle-box {
    position: absolute;
    left: 0;
    top: 851px;
    width: 255px;
    height: 280px;
    background: var(--ink);
    color: var(--white);
    font-family: "Playfair Display", serif;
    padding: 36px 0 0 42px;
    line-height: 1.18;
  }
  .subtitle-box .lead { display: block; font-size: 32px; letter-spacing: 0.02em; }
  .subtitle-box .small { display: block; font-size: 21px; }
  .subtitle-box .caps { display: block; font-size: 25px; letter-spacing: 0.03em; }
  .web-band {
    position: absolute;
    left: 0;
    top: 1195px;
    width: 559px;
    height: 52px;
    background: var(--gold);
  }
  .web-address {
    position: absolute;
    left: 0;
    width: 480px;
    top: 14px;
    text-align: center;
    font-family: "Playfair Display", serif;
    font-size: 18px;
    letter-spacing: 0.14em;
    color: var(--white);
  }
</style>
</head>
<body>
  <div class="canvas">
    <section class="cover">
      <div class="cover-photo" role="img" aria-label="Fashion photograph of two men in light linen and knit summer clothing against a warm taupe studio backdrop"></div>
      <h1 class="title-primary">THE QUIET</h1>
      <div class="title-accent">LEDGER</div>
      <p class="subtitle-box">
        <span class="lead">NOTES</span>
        <span class="small">on slowing</span>
        <span class="caps">THE DAILY</span>
        <span class="caps">RUSH &amp;</span>
        <span class="small">shaping a calmer</span>
        <span class="small">household rhythm</span>
      </p>
      <div class="web-band">
        <span class="web-address">www.brindlequarry.com</span>
      </div>
    </section>
  </div>
</body>
</html>
```